New Business Card (to reflect updated website content and graphics)

I changed some text and graphics on my website, so I need a new business card.

Target Market(s)

Mostly women, ages 30 - 60.

Industry/Entity Type

Life Coaching

Contact Information for Business Card

Included in attached Word document

Font styles to use
Sans Serif

Requirements
Must have
• I am not a creative person, so I will defer to designer. Take a look at my website, and you can get a feel for me, my style, and my target audience. Thank You!

My 3 branding colors are included in attached Word document.

```html
<!DOCTYPE html>
<html lang="en">
<head>
<meta charset="utf-8">
<title>Tide to Hope Coaching – Business Card</title>
<link rel="stylesheet" href="https://fonts.googleapis.com/css2?family=Montserrat:wght@500;700&family=Roboto:wght@400&display=swap">
<style>
  :root {
    --backdrop: #2b2b2b;
    --card-white: #ffffff;
    --teal: #2b97b1;
    --teal-light: #3aa3bb;
    --art-teal: #2e8fae;
    --art-teal-soft: #5fb0c8;
    --ink-light: #ffffff;
  }
  * { margin: 0; padding: 0; box-sizing: border-box; }
  html, body {
    width: 1200px; height: 900px; overflow: hidden;
    background: var(--backdrop);
  }
  .canvas {
    position: relative; width: 1200px; height: 900px;
    display: flex; flex-direction: column; align-items: center; justify-content: center; gap: 36px;
  }
  .card {
    width: 700px; height: 400px; border-radius: 26px;
    position: relative; overflow: hidden;
  }
  .card-front {
    background: var(--card-white);
    display: flex; align-items: center; justify-content: center;
  }
  .word-cloud-area {
    width: 380px; height: 290px; border-radius: 12px;
    background: linear-gradient(180deg, var(--art-teal-soft) 0%, var(--art-teal) 100%);
    opacity: 0.85;
  }
  .card-back {
    background: linear-gradient(135deg, var(--teal) 0%, var(--teal-light) 55%, var(--teal) 100%);
    color: var(--ink-light);
    text-align: center;
    padding-top: 62px;
  }
  .brand-name {
    font-family: "Montserrat", sans-serif; font-weight: 500;
    font-size: 30px; letter-spacing: 6px; text-transform: uppercase;
  }
  .person-name {
    margin-top: 44px;
    font-family: "Montserrat", sans-serif; font-weight: 700;
    font-size: 34px; letter-spacing: 4px; text-transform: uppercase;
  }
  .person-title {
    font-family: "Roboto", sans-serif; font-size: 19px; line-height: 24px;
  }
  .divider {
    margin: 22px auto 0; width: 600px;
    display: flex; align-items: center; gap: 10px;
  }
  .divider-line { flex: 1; height: 1px; background: rgba(255,255,255,0.8); }
  .contact-icon { width: 28px; height: 28px; }
  .contact-phone, .contact-links {
    font-family: "Roboto", sans-serif; font-size: 21px; line-height: 28px;
  }
  .contact-phone { margin-top: 14px; }
</style>
</head>
<body>
<main class="canvas">
  <section class="card card-front">
    <div class="word-cloud-area" role="img" aria-label="Heart-shaped word cloud of coaching words such as hope, love, joy, peace and clarity, with the slogan Feel Better, Live Well across the middle"></div>
  </section>

  <section class="card card-back">
    <p class="brand-name">Tide to Hope Coaching</p>
    <h1 class="person-name">Mara Ellison</h1>
    <p class="person-title">Certified Professional Life Coach | Health &amp; Wellness Coach</p>
    <p class="person-title">Advanced Grief Support Method Specialist</p>
    <div class="divider">
      <span class="divider-line"></span>
      <svg class="contact-icon" viewBox="0 0 28 28" aria-label="Phone">
        <circle cx="14" cy="14" r="12.5" fill="none" stroke="#fff" stroke-width="1.4"/>
        <path d="M10 8 l3 0 l1 4 l-2 1.5 q1.5 3 4 4 l1.5 -2 l4 1 l0 3 q-8 1 -11.5 -11.5 z" fill="none" stroke="#fff" stroke-width="1.2"/>
      </svg>
      <svg class="contact-icon" viewBox="0 0 28 28" aria-label="Email">
        <circle cx="14" cy="14" r="12.5" fill="none" stroke="#fff" stroke-width="1.4"/>
        <rect x="8" y="9.5" width="12" height="9" fill="none" stroke="#fff" stroke-width="1.2"/>
        <path d="M8 9.5 L14 15 L20 9.5" fill="none" stroke="#fff" stroke-width="1.2"/>
      </svg>
      <svg class="contact-icon" viewBox="0 0 28 28" aria-label="Website">
        <circle cx="14" cy="14" r="12.5" fill="none" stroke="#fff" stroke-width="1.4"/>
        <circle cx="14" cy="14" r="7" fill="none" stroke="#fff" stroke-width="1.1"/>
        <ellipse cx="14" cy="14" rx="3" ry="7" fill="none" stroke="#fff" stroke-width="1.1"/>
        <path d="M7 14 H21" stroke="#fff" stroke-width="1.1"/>
      </svg>
      <span class="divider-line"></span>
    </div>
    <p class="contact-phone">(555) 014-2739</p>
    <p class="contact-links">mara@tidetohopecoaching.com | www.tidetohopecoaching.com</p>
  </section>
</main>
</body>
</html>
```